Marlow Creek sign

24"x36" sign for new home construction job site. Located in affluent in-town neighborhood in Midwest. Traditional american style homes. 2nd generation construction company. Sign needs to convey strength and elegance but not overly elaborate. Competition most has signs consisting of text.

Sign text reads:
Marlow Creek Builders
Custom Luxury for Over 20 years
248-555-0137

Target Market(s)

Upper middle income home buyers

Industry/Entity Type

Construction

Font styles to use
Serif
Decorative

Requirements
Must have
• Logo image no more than 2 colors
Nice to have
• Should be visible and legible from distance of 30'
Should not have
• Not just image of house as logo

```html
<!DOCTYPE html>
<html lang="en">
<head>
<meta charset="utf-8">
<title>Marlow Creek Builders – Job Site Sign</title>
<link rel="stylesheet" href="https://fonts.googleapis.com/css2?family=Della+Respira&family=Libre+Baskerville:wght@700&display=swap">
<style>
  :root {
    --page: #ffffff;
    --plaque: #e8c886;
    --ink: #141414;
  }
  html, body {
    margin: 0;
    padding: 0;
    width: 1200px;
    height: 911px;
    overflow: hidden;
    background: var(--page);
  }
  .sign {
    position: relative;
    width: 1200px;
    height: 911px;
  }
  .sign__plaque {
    position: absolute;
    inset: 0;
    width: 1200px;
    height: 911px;
  }
  .sign__plaque-shape {
    fill: var(--plaque);
    stroke: var(--ink);
    stroke-width: 5;
  }
  .sign__name {
    position: absolute;
    left: 0;
    width: 1200px;
    margin: 0;
    text-align: center;
    font-family: "Della Respira", Georgia, serif;
    font-weight: 400;
    color: var(--ink);
    line-height: 1;
  }
  .sign__name-line {
    position: absolute;
    left: 0;
    width: 1200px;
    font-size: 84px;
    letter-spacing: 1px;
  }
  .sign__name-line--first { top: 258px; }
  .sign__name-line--second { top: 360px; }
  .sign__tagline {
    position: absolute;
    top: 514px;
    left: 0;
    width: 1200px;
    margin: 0;
    text-align: center;
    font-family: "Della Respira", Georgia, serif;
    font-size: 56px;
    line-height: 1;
    color: var(--ink);
  }
  .sign__contact {
    position: absolute;
    top: 636px;
    left: 0;
    width: 1200px;
    display: flex;
    justify-content: center;
    align-items: center;
    gap: 22px;
  }
  .sign__phone-icon {
    width: 56px;
    height: 90px;
    fill: var(--ink);
  }
  .sign__phone-number {
    font-family: "Libre Baskerville", Georgia, serif;
    font-weight: 700;
    font-size: 80px;
    line-height: 1;
    color: var(--ink);
  }
</style>
</head>
<body>
  <main class="sign">
    <svg class="sign__plaque" viewBox="0 0 1000 759" aria-hidden="true">
      <path class="sign__plaque-shape" d="
        M 235 93 H 765
        A 70 70 0 0 1 835 163
        Q 835 183 855 183
        H 890 A 50 50 0 0 1 940 233
        V 533 A 50 50 0 0 1 890 583
        H 855 Q 835 583 835 603
        A 65 65 0 0 1 770 668
        H 230
        A 65 65 0 0 1 165 603
        Q 165 583 145 583
        H 110 A 50 50 0 0 1 60 533
        V 233 A 50 50 0 0 1 110 183
        H 145 Q 165 183 165 163
        A 70 70 0 0 1 235 93 Z"/>
    </svg>

    <h1 class="sign__name">
      <span class="sign__name-line sign__name-line--first">MARLOW CREEK</span>
      <span class="sign__name-line sign__name-line--second">BUILDERS</span>
    </h1>

    <p class="sign__tagline">Custom Luxury for Over 20 Years..</p>

    <div class="sign__contact">
      <svg class="sign__phone-icon" viewBox="0 0 56 90" aria-hidden="true">
        <path d="M20 4 C10 6 4 20 4 44 C4 68 10 82 20 86 L28 86 C31 86 32 84 32 81 L30 64 C30 61 28 60 25 60 L19 60 C17 52 17 38 19 30 L25 30 C28 30 30 29 30 26 L32 9 C32 6 31 4 28 4 Z"/>
      </svg>
      <span class="sign__phone-number">248-555-0137</span>
    </div>
  </main>
</body>
</html>
```